Copper Lantern Gin

The gin is 100% proof and men and anbody 18 - 30 year old will be a target market - the bottle is very distinctive and lends itself to a square label.

The bottle is curved with a large front face that lends itself to a striking design. There should be enough space around the label to show the black gin in the bottle as this is a feature.

The current bottle with the existing label is attached below as is the new glass bottle. The new gin will be coloured black.

Font styles to use
Decorative
Script

```html
<!DOCTYPE html>
<html lang="en">
<head>
<meta charset="utf-8">
<title>Copper Lantern Gin – Label</title>
<link rel="stylesheet" href="https://fonts.googleapis.com/css2?family=Cinzel:wght@600&family=Pinyon+Script&family=Cormorant+Garamond:wght@500&display=swap">
<style>
  :root {
    --backdrop: #f4f4f2;
    --label-black: #060606;
    --gold: #c2a566;
    --gold-deep: #8a6e35;
    --gold-soft: #a88d52;
  }
  * { box-sizing: border-box; margin: 0; padding: 0; }
  html, body {
    width: 968px;
    height: 1200px;
    overflow: hidden;
    background: var(--backdrop);
  }
  .canvas {
    position: relative;
    width: 968px;
    height: 1200px;
  }
  .label {
    position: absolute;
    left: 70px;
    top: 156px;
    width: 828px;
    height: 888px;
    background: var(--label-black);
    color: var(--gold);
  }
  .label-frame {
    position: absolute;
    inset: 12px;
    border: 1.5px solid var(--gold-soft);
  }
  .label-frame-inner {
    position: absolute;
    inset: 20px;
    border: 1px solid var(--gold-deep);
  }
  .proof {
    position: absolute;
    right: 58px;
    top: 50px;
    font-family: "Pinyon Script", cursive;
    font-size: 30px;
    color: var(--gold-soft);
  }
  .crest {
    position: absolute;
    left: 289px;
    top: 80px;
    width: 250px;
    height: 124px;
    border-radius: 50% / 48%;
    background: radial-gradient(ellipse at center, #6b5530 0%, #3a2d17 55%, rgba(6,6,6,0) 78%);
  }
  .brand-name {
    position: absolute;
    left: 0;
    right: 0;
    top: 300px;
    text-align: center;
    font-family: "Cinzel", serif;
    font-weight: 600;
    font-size: 50px;
    letter-spacing: 2px;
    color: var(--gold);
  }
  .product-line {
    position: absolute;
    left: 100px;
    right: 100px;
    top: 368px;
    display: flex;
    align-items: center;
    gap: 28px;
  }
  .rule {
    flex: 1;
    height: 7px;
    border-top: 1.5px solid var(--gold);
    border-bottom: 1.5px solid var(--gold);
  }
  .product-type {
    font-family: "Cinzel", serif;
    font-weight: 600;
    font-size: 84px;
    line-height: 1;
    letter-spacing: 3px;
    color: var(--gold);
  }
  .style-note {
    position: absolute;
    left: 0;
    right: 0;
    top: 530px;
    text-align: center;
    font-family: "Pinyon Script", cursive;
    font-size: 34px;
    color: var(--gold-soft);
  }
  .spec {
    position: absolute;
    bottom: 44px;
    font-family: "Cormorant Garamond", serif;
    font-weight: 500;
    font-size: 19px;
    color: var(--gold-deep);
  }
  .spec-abv { left: 46px; }
  .spec-volume { right: 48px; }
</style>
</head>
<body>
  <div class="canvas">
    <div class="label">
      <div class="label-frame"></div>
      <div class="label-frame-inner"></div>
      <div class="proof">100% Proof</div>
      <div class="crest" role="img" aria-label="Gold ornamental crest framing a hound illustration"></div>
      <div class="brand-name">Copper Lantern</div>
      <div class="product-line">
        <span class="rule"></span>
        <span class="product-type">GIN</span>
        <span class="rule"></span>
      </div>
      <div class="style-note">Navy Strength British Gin</div>
      <div class="spec spec-abv">57%abv</div>
      <div class="spec spec-volume">750ML</div>
    </div>
  </div>
</body>
</html>
```